Boutique personal training and fitness studio - banner ad design

We need a 'revolving' banner ad designed for our personal training and fitness studio. There are three separate offers (i.e. 3 pages to the advertisements)
Offer 1
PT Starter Pack
3 personal training sessions
$119
New clients only
Offer 2
Group fitness
2 weeks unlimited group fitness classes
$29
New clients only
Offer 3
Strength starter pack
2 weeks unlimited group fitness classes and 2 PT sessions
$89
New clients only
Please do not put the words "Offer 1, 2 or 3" in the ads - just the text following each offer.
Each advertisement should be sized to fit across around half of the webpage and be in landscape format.
Each advertisement should have a suitable picture (no cartoons) and should be complimentary to the existing website.
Each advertisement should also include the logo (attached)
www.corrabankliftworks.com.au
Training

```html
<!DOCTYPE html>
<html lang="en">
<head>
<meta charset="utf-8">
<title>Banner Ad: Corrabank Liftworks</title>
<link rel="stylesheet" href="https://fonts.googleapis.com/css2?family=Russo+One&family=Roboto+Condensed:ital,wght@0,700;0,800;1,400&family=Montserrat:wght@400;700&display=swap">
<style>
  :root {
    --board: #ffffff;
    --red-deep: #8e0a0c;
    --red: #c1161a;
    --headline: #fff200;
    --ink-light: #ffffff;
    --photo-dark: #2b2b2b;
    --photo-mid: #7a7a7a;
    --photo-light: #c9c9c9;
    --btn-top: #f7a53a;
    --btn-bottom: #d86a0b;
    --footer-top: #3a3a3a;
    --footer-bottom: #1c1c1c;
    --footer-accent: #ffc20e;
  }
  * { margin: 0; padding: 0; box-sizing: border-box; }
  html, body { width: 900px; height: 1200px; overflow: hidden; }
  body { background: var(--board); position: relative; font-family: "Roboto Condensed", Arial, sans-serif; }

  .banner {
    position: absolute; left: 194px; width: 533px; height: 265px;
    display: flex; box-shadow: 0 4px 10px rgba(0,0,0,.28); overflow: hidden;
  }
  .banner--pt { top: 73px; }
  .banner--group { top: 386px; }
  .banner--strength { top: 699px; }

  .banner__photo { height: 100%; }
  .banner__photo--left { width: 144px; background: linear-gradient(160deg, var(--photo-mid), var(--photo-dark) 75%); }
  .banner__photo--right { width: 142px; background: linear-gradient(200deg, var(--photo-light), var(--photo-mid) 45%, var(--photo-dark)); position: relative; }

  .banner__offer {
    width: 247px; height: 100%;
    background: linear-gradient(180deg, var(--red) 0%, var(--red-deep) 100%);
    display: flex; flex-direction: column; align-items: center; text-align: center;
    color: var(--ink-light);
  }
  .offer__title {
    font-family: "Russo One", Impact, sans-serif; color: var(--headline);
    font-size: 29px; line-height: 33px; text-shadow: 0 2px 3px rgba(0,0,0,.35);
  }
  .offer__detail { font-weight: 700; font-size: 15px; line-height: 23px; }
  .offer__price {
    font-weight: 800; font-size: 68px; line-height: 64px; letter-spacing: -1px;
    text-shadow: 0 3px 4px rgba(0,0,0,.45); position: relative; padding-left: 16px;
  }
  .offer__price sup { font-size: 24px; position: absolute; left: 0; top: 4px; }
  .offer__cta {
    margin-top: 6px; width: 120px; height: 28px; border-radius: 4px;
    background: linear-gradient(180deg, var(--btn-top), var(--btn-bottom));
    font-weight: 800; font-size: 18px; line-height: 28px; color: var(--ink-light);
    text-shadow: 0 1px 2px rgba(0,0,0,.35); box-shadow: 0 2px 3px rgba(0,0,0,.35);
  }
  .offer__note { margin-top: 8px; font-style: italic; font-weight: 400; font-size: 11px; }

  .brand-tag {
    position: absolute; left: 19px; top: 199px; width: 107px; height: 49px;
    background: #000; display: flex; align-items: center; justify-content: center;
    font-weight: 800; font-size: 14px; color: var(--ink-light); text-transform: uppercase; letter-spacing: .5px;
    text-align: center; line-height: 15px;
  }

  .banner--pt .banner__offer { padding-top: 20px; }
  .banner--group .banner__offer { padding-top: 38px; }
  .banner--strength .banner__offer { padding-top: 12px; }

  .board-footer {
    position: absolute; left: 0; top: 1040px; width: 900px; height: 160px;
    background: linear-gradient(180deg, var(--footer-top), var(--footer-bottom));
  }
  .board-footer__label {
    position: absolute; left: 47px; top: 72px;
    font-family: "Montserrat", Arial, sans-serif; font-size: 20px; color: var(--ink-light);
  }
  .board-footer__label strong { color: var(--footer-accent); font-weight: 700; }
</style>
</head>
<body>

<section class="banner banner--pt">
  <div class="banner__photo banner__photo--left" role="img" aria-label="Athlete training in a gym"></div>
  <div class="banner__offer">
    <h2 class="offer__title">PT STARTER<br>PACK</h2>
    <p class="offer__detail">3 personal training sessions</p>
    <p class="offer__price"><sup>$</sup>119</p>
    <div class="offer__cta">JOIN NOW</div>
    <p class="offer__note">New clients only!</p>
  </div>
  <div class="banner__photo banner__photo--right" role="img" aria-label="Gym rig with hanging rings">
    <div class="brand-tag">Corrabank<br>Liftworks</div>
  </div>
</section>

<section class="banner banner--group">
  <div class="banner__photo banner__photo--left" role="img" aria-label="Group fitness class in action"></div>
  <div class="banner__offer">
    <h2 class="offer__title">GROUP FITNESS</h2>
    <p class="offer__detail">2 weeks unlimited<br>group fitness classes</p>
    <p class="offer__price"><sup>$</sup>29</p>
    <div class="offer__cta">JOIN NOW</div>
    <p class="offer__note">New clients only!</p>
  </div>
  <div class="banner__photo banner__photo--right" role="img" aria-label="Members exercising in the studio">
    <div class="brand-tag">Corrabank<br>Liftworks</div>
  </div>
</section>

<section class="banner banner--strength">
  <div class="banner__photo banner__photo--left" role="img" aria-label="Athlete doing floor exercises"></div>
  <div class="banner__offer">
    <h2 class="offer__title">STRENGTH<br>STARTER PACK</h2>
    <p class="offer__detail">2 weeks unlimited group fitness<br>classes and 2 PT sessions</p>
    <p class="offer__price"><sup>$</sup>89</p>
    <div class="offer__cta">JOIN NOW</div>
    <p class="offer__note">New clients only!</p>
  </div>
  <div class="banner__photo banner__photo--right" role="img" aria-label="Group doing floor workout">
    <div class="brand-tag">Corrabank<br>Liftworks</div>
  </div>
</section>

<footer class="board-footer">
  <p class="board-footer__label"><strong>Banner Ad:</strong> Corrabank Liftworks</p>
</footer>

</body>
</html>
```